Global social media analytics company needs business card design

We need an updated business card design to align with our new website - brightquillo.net -

I would also like a favicon designed as well.

Target Market(s)

CEOs, CMOs go big companies

Industry/Entity Type

Business

Contact Information for Business Card

Room for the following:
Address
Main telephone
Direct telephone or cell phone
twitter handle

Colors
aaaaaa

Requirements
Must have
• Attention to detail; style.
• Use the logo color from our website - which is gray

```html
<!DOCTYPE html>
<html lang="en">
<head>
<meta charset="utf-8">
<title>Brightquillo Business Card</title>
<link href="https://fonts.googleapis.com/css2?family=Roboto:wght@400;700&display=swap" rel="stylesheet">
<style>
  :root {
    --brand-grey: #aaaaaa;
    --text-dark: #555555;
    --text-mid: #666666;
    --card-white: #ffffff;
    --card-edge: #7a7a7a;
    --backdrop: #ece9e4;
    --rule: #b5b5b5;
  }
  * { margin: 0; padding: 0; box-sizing: border-box; }
  html, body {
    width: 1173px; height: 1200px; overflow: hidden;
    background: var(--backdrop);
    font-family: "Roboto", Arial, sans-serif;
  }
  .card {
    position: absolute; left: 117px; width: 877px; height: 501px;
    background: var(--card-white); border: 1px solid var(--card-edge);
  }
  .card--front { top: 69px; }
  .card--back { top: 627px; }

  .brand { position: absolute; left: 115px; top: 46px; display: flex; align-items: center; }
  .card--back .brand { left: 110px; top: 166px; }
  .brand__dot { width: 166px; height: 166px; border-radius: 50%; background: var(--brand-grey); }
  .brand__name {
    margin-left: 24px; font-size: 72px; font-weight: 700;
    color: var(--brand-grey); letter-spacing: -1px; line-height: 1;
  }

  .identity {
    position: absolute; right: calc(877px - 441px); top: 308px;
    text-align: right; color: var(--text-mid);
  }
  .identity__name { font-size: 28px; font-weight: 700; color: var(--text-dark); line-height: 34px; }
  .identity__title { font-size: 23px; font-weight: 400; }
  .identity__company { margin-top: 22px; font-size: 23px; font-weight: 700; line-height: 30px; }
  .identity__address { font-size: 23px; line-height: 29px; }

  .divider {
    position: absolute; left: 461px; top: 308px; width: 2px; height: 142px;
    background: linear-gradient(to bottom, transparent, var(--rule) 20%, var(--rule) 80%, transparent);
  }

  .contacts { position: absolute; left: 494px; top: 310px; list-style: none; color: var(--text-dark); }
  .contacts li { display: flex; align-items: center; height: 37px; font-size: 23px; }
  .contacts svg { width: 20px; height: 20px; margin-right: 14px; flex: none; }
  .contacts .icon-fill { fill: var(--brand-grey); }
</style>
</head>
<body>
  <section class="card card--front">
    <div class="brand">
      <div class="brand__dot"></div>
      <span class="brand__name">brightquillo</span>
    </div>

    <div class="identity">
      <p class="identity__name">Your Name, <span class="identity__title">Title</span></p>
      <p class="identity__company">BRIGHTQUILLO, INC.</p>
      <p class="identity__address">1875 Harborview Ave. 3rd Fl</p>
      <p class="identity__address">Easton, MA 02356, USA</p>
    </div>

    <div class="divider"></div>

    <ul class="contacts">
      <li>
        <svg viewBox="0 0 20 20" aria-hidden="true">
          <circle cx="10" cy="10" r="9" fill="none" stroke="#aaaaaa" stroke-width="1.4"/>
          <path class="icon-fill" d="M7 5 L9 7 L8 9 C8.6 10.6 9.6 11.6 11 12 L13 11 L15 13 L13.5 15 C9 14.5 5.5 11 5 6.5 Z"/>
        </svg>
        +1 555 014 2290
      </li>
      <li>
        <svg viewBox="0 0 20 20" aria-hidden="true">
          <rect x="5" y="3" width="10" height="16" rx="1.5" fill="none" stroke="#aaaaaa" stroke-width="1.6"/>
          <rect class="icon-fill" x="7" y="5.5" width="6" height="4"/>
          <rect class="icon-fill" x="7" y="11" width="6" height="6" opacity=".7"/>
          <rect class="icon-fill" x="12" y="0.5" width="1.5" height="3"/>
        </svg>
        +123 456 7890
      </li>
      <li>
        <svg viewBox="0 0 20 20" aria-hidden="true">
          <rect class="icon-fill" x="1" y="4" width="18" height="13" rx="1"/>
          <path d="M1.5 5 L10 11.5 L18.5 5" fill="none" stroke="#ffffff" stroke-width="1.6"/>
        </svg>
        info@brightquillo.net
      </li>
      <li>
        <svg viewBox="0 0 20 20" aria-hidden="true">
          <circle class="icon-fill" cx="10" cy="10" r="8"/>
        </svg>
        @brightquillo
      </li>
    </ul>
  </section>

  <section class="card card--back">
    <div class="brand">
      <div class="brand__dot"></div>
      <span class="brand__name">brightquillo</span>
    </div>
  </section>
</body>
</html>
```